Im looking to drive the very foundation of our business into a differnet direction. With a team of

We need to develop firstly a corporate profile that really gets the attentions of the reader. From here I want then to develop a report format (template) that we can overlay the reports we do. We have a logo and tat that can be found at www.kestrelworkgroup.com.au. I want to stay with the lime green and blue to be sure we stay on the same branding message we already have.

The final design should communicate as the business is named Marlow Brindle Consulting Australia.

https://www.filecrate.example/s/k27vq8mzt4pwbxe/pixelgrove_462915038.jpg?dl=0

Target Market(s)

Large corporate clents

Industry/Entity Type

Consulting

Requirements
Must have
• Photos not animated pictures

```html
<!DOCTYPE html>
<html lang="en">
<head>
<meta charset="utf-8">
<title>Marlow Brindle Consulting – Corporate Profile and Report Template</title>
<link rel="stylesheet" href="https://fonts.googleapis.com/css2?family=Arimo:wght@400;700&display=swap">
<style>
  :root {
    --backdrop: #cbcbcb;
    --paper: #ffffff;
    --brand-blue: #25377d;
    --brand-lime: #7cc242;
    --rule-green: #8cc84b;
    --text-grey: #333333;
    --tile-hygiene: #7dc45a;
    --tile-ohs: #4f7fac;
    --tile-enviro: #f6bd3c;
    --tile-lab: #a6d152;
    --tile-property: #629fd4;
    --tile-programs: #e6dc44;
  }
  * { margin: 0; padding: 0; box-sizing: border-box; }
  html, body { width: 1200px; height: 1000px; overflow: hidden; }
  body {
    background: var(--backdrop);
    font-family: "Arimo", Arial, sans-serif;
    position: relative;
  }
  .page {
    position: absolute;
    top: 115px;
    width: 544px;
    height: 769px;
    background: var(--paper);
  }
  .page--profile { left: 30px; }
  .page--report { left: 613px; }

  .brand {
    position: absolute;
    display: flex;
    align-items: center;
    gap: 10px;
    color: var(--brand-blue);
    font-weight: 700;
    white-space: nowrap;
  }
  .brand__dot {
    border-radius: 50%;
    background: var(--brand-lime);
    flex: none;
  }
  .page--profile .brand { left: 32px; top: 46px; width: 346px; font-size: 24px; letter-spacing: -0.4px; }
  .page--profile .brand__dot { width: 44px; height: 44px; }
  .page--report .brand { left: 30px; top: 36px; font-size: 22px; letter-spacing: -0.4px; }
  .page--report .brand__dot { width: 36px; height: 36px; }

  .photo-team {
    position: absolute;
    left: 386px; top: 28px;
    width: 124px; height: 79px;
    background: linear-gradient(160deg, #dfe7ee 0%, #b9c9a0 55%, #8d9a6a 100%);
  }
  .rule {
    position: absolute;
    height: 2px;
  }
  .rule--blue { background: var(--brand-blue); }
  .rule--green { background: var(--rule-green); }

  .services {
    position: absolute;
    left: 64px; top: 158px;
    display: grid;
    grid-template-columns: repeat(3, 127px);
    grid-auto-rows: 134px;
    column-gap: 18px;
    row-gap: 19px;
  }
  .service {
    padding: 11px 12px;
    color: #fff;
    font-weight: 700;
    font-size: 12px;
    line-height: 15px;
  }
  .service--hygiene { background: var(--tile-hygiene); }
  .service--ohs { background: var(--tile-ohs); }
  .service--enviro { background: var(--tile-enviro); }
  .service--lab { background: var(--tile-lab); }
  .service--property { background: var(--tile-property); }
  .service--programs { background: var(--tile-programs); }

  .photo-presenter {
    position: absolute;
    left: 170px; top: 463px;
    width: 195px; height: 92px;
    background: linear-gradient(180deg, #e9e9e9 0%, #9a9a9a 45%, #2d2f36 100%);
  }

  .head-office {
    position: absolute;
    left: 0; width: 544px; top: 585px;
    text-align: center;
    color: var(--text-grey);
  }
  .head-office__title {
    color: var(--brand-blue);
    font-size: 13px;
    font-weight: 700;
    margin-bottom: 12px;
  }
  .head-office__line {
    font-size: 9.5px;
    font-weight: 700;
    line-height: 12px;
  }
  .head-office__gap { height: 5px; }

  .footer-mark {
    position: absolute;
    left: 247px; top: 682px;
    width: 50px;
    display: flex;
    flex-direction: column;
    align-items: center;
    gap: 4px;
    color: var(--brand-blue);
    font-weight: 700;
    font-size: 13px;
  }
  .footer-mark__dot {
    width: 30px; height: 30px;
    border-radius: 50%;
    background: var(--brand-lime);
  }
</style>
</head>
<body>

<section class="page page--profile" aria-label="Corporate profile cover">
  <div class="brand"><span class="brand__dot"></span>Marlow Brindle Consulting</div>
  <div class="photo-team" role="img" aria-label="Photo of two site workers in hard hats and hi-vis vests reviewing plans"></div>
  <div class="rule rule--blue" style="left:32px; top:107px; width:480px;"></div>

  <div class="services">
    <div class="service service--hygiene">Occupational<br>Hygiene</div>
    <div class="service service--ohs">Occupational<br>Health and Safety</div>
    <div class="service service--enviro">Environmental<br>Solutions</div>
    <div class="service service--lab">Laboratory</div>
    <div class="service service--property">Property<br>Services</div>
    <div class="service service--programs">WellStep<br>Programs</div>
  </div>

  <div class="photo-presenter" role="img" aria-label="Photo of a businessman in a suit leaning over the rule and pointing down"></div>
  <div class="rule rule--blue" style="left:32px; top:554px; width:480px;"></div>

  <div class="head-office">
    <p class="head-office__title">HEAD OFFICE</p>
    <p class="head-office__line">48 Garrick Street,</p>
    <p class="head-office__line">Torrens Park, SA, 5062</p>
    <div class="head-office__gap"></div>
    <p class="head-office__line">Phone:&nbsp; (08) 7420 3316</p>
    <p class="head-office__line">Fax:&nbsp; (08) 7420 3390</p>
  </div>

  <div class="footer-mark"><span class="footer-mark__dot"></span>MBC</div>
  <div class="rule rule--green" style="left:50px; top:719px; width:197px;"></div>
  <div class="rule rule--green" style="left:297px; top:719px; width:197px;"></div>
  <div class="rule rule--green" style="left:32px; top:729px; width:215px;"></div>
  <div class="rule rule--green" style="left:297px; top:729px; width:215px;"></div>
</section>

<section class="page page--report" aria-label="Report template page">
  <div class="brand"><span class="brand__dot"></span>Marlow Brindle Consulting</div>
  <div class="rule rule--green" style="left:37px; top:88px; width:273px;"></div>
  <div class="rule rule--green" style="left:417px; top:77px; width:89px;"></div>
  <div class="rule rule--green" style="left:392px; top:82px; width:114px;"></div>
  <div class="rule rule--green" style="left:372px; top:88px; width:134px;"></div>
  <div class="rule rule--blue" style="left:31px; top:94px; width:481px;"></div>

  <div class="footer-mark"><span class="footer-mark__dot"></span>MBC</div>
  <div class="rule rule--green" style="left:50px; top:719px; width:197px;"></div>
  <div class="rule rule--green" style="left:297px; top:719px; width:197px;"></div>
  <div class="rule rule--green" style="left:32px; top:729px; width:215px;"></div>
  <div class="rule rule--green" style="left:297px; top:729px; width:215px;"></div>
</section>

</body>
</html>
```